Aviation security consulting company needs a website

We need a website design for Brisk Holloway, and aviation security consulting company. Brisk Holloway (www.briskholloway.example) is an aviation security consulting company that works with government and industry stakeholders in over 60 countries on aviation security strategy, governance, and oversight at the regulatory and operational level.
Brisk Holloway is strongly internationally focused.
The website required should be simple, corporate, serious, and communicate professionalism, reliability and honesty. We are trying to give the company a feeling of being well established.
The attached files include the company logo, along with examples of company web page styles that we like.
The Brisk Holloway website need only be around five pages long (landing page, who we are, our services, our clients, contact), though don't feel limited to only five pages.
The existing website (www.briskholloway.example) was rushed and put together using Wix. We don't love the existing website as it looks too amateur, so don't use it as a template.
There is no requirement for any online sales tools to be included in the site. The site is purely informational, with the option of people making contact via email.

```html
<!DOCTYPE html>
<html lang="en">
<head>
<meta charset="utf-8">
<title>Brisk Holloway — Aviation Security Consulting</title>
<link href="https://fonts.googleapis.com/css2?family=Arimo:wght@400;700&family=Open+Sans:ital,wght@0,400;0,600;0,700;1,400&display=swap" rel="stylesheet">
<style>
:root{
  --navy:#1b2d6b;
  --navy-dark:#14224f;
  --ink:#222;
  --text:#666;
  --light:#f1f1f1;
  --footer:#222;
  --footer-text:#ccc;
  --white:#fff;
}
*{box-sizing:border-box;margin:0;padding:0}
html,body{width:1200px;height:2880px;overflow:hidden;background:#fff}
body{font-family:"Open Sans",Arial,sans-serif;color:var(--text);position:relative}
.abs{position:absolute}
.page{position:relative;width:1200px;height:2880px;overflow:hidden}
h1,h2,h3,h4{font-family:"Arimo",Arial,sans-serif;color:var(--ink)}

/* header */
.header{position:absolute;left:0;top:0;width:1200px;height:96px;background:#fff;border-top:4px solid var(--navy)}
.brand{position:absolute;left:100px;top:14px;display:flex;align-items:center;gap:12px}
.brand-mark{width:66px;height:66px;background:var(--navy)}
.brand-name{font-family:"Arimo",Arial,sans-serif;font-weight:700;font-size:36px;color:var(--navy);line-height:1;white-space:nowrap}
.brand-tag{font-size:15px;color:var(--navy);letter-spacing:1px;margin-top:2px;white-space:nowrap}
.contact-strip{position:absolute;left:570px;top:18px;display:flex;align-items:center;gap:26px;font-size:15px;color:var(--ink);font-weight:600;white-space:nowrap}
.contact-strip span{display:flex;align-items:center;gap:10px}
.social{display:flex;gap:8px}
.social i{display:block;width:28px;height:28px;border:1.5px solid var(--navy);border-radius:50%}
.nav{position:absolute;left:541px;top:58px;width:579px;height:38px;background:#111;display:flex;font-family:"Arimo",Arial,sans-serif;font-weight:700;font-size:15px}
.nav a{flex:1 1 auto;color:#fff;text-decoration:none;padding:0 12px;line-height:38px;text-align:center;white-space:nowrap}
.nav a.active{background:var(--navy);padding:0 26px}

/* hero */
.hero{position:absolute;left:0;top:96px;width:1200px;height:422px;background:linear-gradient(180deg,#7b7a80 0%,#c8a98b 35%,#8d8e93 60%,#4b4d52 100%)}
.hero h1{position:absolute;left:100px;top:134px;font-size:58px;line-height:64px;color:#fff;text-shadow:0 2px 4px rgba(0,0,0,.4);white-space:nowrap}
.hero p{position:absolute;left:100px;top:205px;font-family:"Arimo",Arial,sans-serif;font-size:23px;color:#fff;white-space:nowrap}
.btn{display:flex;align-items:center;background:var(--navy);color:#fff;font-family:"Arimo",Arial,sans-serif;font-weight:700;text-transform:uppercase;text-decoration:none;white-space:nowrap}
.btn .arrow{background:#111;height:100%;display:flex;align-items:center;justify-content:center;clip-path:polygon(18% 0,100% 0,100% 100%,0 100%)}
.hero .btn{position:absolute;left:100px;top:244px;width:171px;height:38px;font-size:15px}
.hero .btn b{padding-left:18px;flex:1}
.hero .btn .arrow{width:52px}
.dots{position:absolute;left:565px;top:368px;display:flex;gap:6px}
.dots i{width:13px;height:13px;border:2px solid #fff;border-radius:50%}
.dots i.on{background:#fff}

/* welcome */
.welcome h2{position:absolute;top:560px;width:1200px;text-align:center;font-size:27px}
.welcome h2 em,.section-title em{font-style:normal;color:var(--navy)}
.welcome .lead{position:absolute;left:220px;top:608px;width:760px;text-align:center;font-size:12.5px;line-height:23px}
.feature{position:absolute;top:690px;width:240px;text-align:center}
.diamond{width:90px;height:90px;margin:14px auto 0;background:var(--navy);transform:rotate(45deg);display:flex;align-items:center;justify-content:center}
.diamond svg{transform:rotate(-45deg)}
.feature h3{margin-top:40px;font-size:17px}
.feature p{margin-top:12px;font-size:12.5px;line-height:23px}
.feature a{display:block;margin-top:12px;font-family:"Arimo",Arial,sans-serif;font-weight:700;font-size:13px;color:var(--navy);text-decoration:none}

/* services */
.services{position:absolute;left:0;top:995px;width:1200px;height:474px;background:var(--light)}
.section-title{font-size:25px}
.services .section-title{position:absolute;left:100px;top:40px}
.pager{position:absolute;top:40px;width:36px;height:36px;border-radius:50%;background:#d6d6d6;display:flex;align-items:center;justify-content:center}
.card{position:absolute;top:99px;width:236px}
.card .pic{height:154px;border:4px solid #fff;box-shadow:0 0 0 1px #ddd}
.card h3{margin-top:16px;font-size:17px;white-space:nowrap}
.card p{margin-top:10px;font-size:12.5px;line-height:20px}
.card .btn{margin-top:18px;width:134px;height:35px;font-size:12px}
.card .btn b{padding-left:11px;flex:1}
.card .btn .arrow{width:40px}

/* testimonial */
.quote{position:absolute;left:0;top:1469px;width:1200px;height:182px;background:var(--navy);color:#fff}
.quote .qmark{position:absolute;left:150px;top:36px;width:110px;height:110px;border-radius:50%;background:#d9d9d9;display:flex;align-items:center;justify-content:center;font-family:Georgia,serif;font-size:110px;color:#fff;line-height:1;padding-top:44px}
.quote .portrait{position:absolute;left:234px;top:34px;width:96px;height:112px;border-radius:50%;background:linear-gradient(160deg,#e8e8e8,#9aa0ab);border:3px solid #fff}
.quote blockquote{position:absolute;left:365px;top:38px;width:705px;font-style:italic;font-size:13.5px;line-height:24px}
.quote cite{position:absolute;left:365px;top:118px;font-style:normal;font-family:"Arimo",Arial,sans-serif;font-weight:700;font-size:14px}
.chev{position:absolute;top:78px}

/* industries */
.industries .section-title{position:absolute;top:1700px;width:1200px;text-align:center;font-size:27px}
.tile{position:absolute;width:327px;height:213px}
.tile span{position:absolute;right:10px;bottom:10px;color:#fff;font-family:"Arimo",Arial,sans-serif;font-weight:700;font-size:15px;text-shadow:0 1px 3px rgba(0,0,0,.7);white-space:nowrap}
.view-more{position:absolute;left:538px;top:2243px;width:126px;height:36px;border:1px solid #ccc;display:flex;align-items:center;justify-content:center;font-family:"Arimo",Arial,sans-serif;font-weight:700;font-size:13px;color:var(--navy);white-space:nowrap}

/* clients */
.clients{position:absolute;left:0;top:2329px;width:1200px;height:244px;background:var(--light)}
.clients .section-title{position:absolute;top:34px;width:1200px;text-align:center;font-size:26px;color:var(--navy)}
.client{position:absolute;top:111px;width:165px;height:79px;background:#fff;border:1px solid #ddd;display:flex;align-items:center;justify-content:center;gap:8px;font-family:"Arimo",Arial,sans-serif;font-weight:700;font-size:14px;color:var(--navy);white-space:nowrap}
.client i{flex:none;width:14px;height:14px;background:var(--navy)}

/* footer */
.footer{position:absolute;left:0;top:2573px;width:1200px;height:307px;background:var(--footer);border-top:5px solid var(--navy);color:var(--footer-text)}
.footer .brand{left:100px;top:87px}
.footer .brand-mark{width:56px;height:56px;background:none;border:4px solid #fff}
.footer .brand-name{color:#fff;font-size:31px}
.footer .brand-tag{color:#fff;font-size:13px}
.footer h4{position:absolute;color:#fff;font-size:17px;top:38px;white-space:nowrap}
.links{position:absolute;left:434px;top:80px;list-style:none;font-size:13px;line-height:29px}
.news p{position:absolute;left:591px;top:78px;width:240px;font-size:12.5px;line-height:19px}
.news .field{position:absolute;left:591px;top:120px;width:263px;height:32px;background:#fff;color:#888;font-size:12px;padding:8px 14px}
.news .subscribe{position:absolute;left:591px;top:168px;width:100px;height:32px;border:2px solid #fff;color:#fff;font-family:"Arimo",Arial,sans-serif;font-weight:700;font-size:13px;display:flex;align-items:center;justify-content:center}
.contact-list{position:absolute;left:916px;top:80px;list-style:none;font-size:12.5px;line-height:19px}
.contact-list li{display:flex;gap:18px;margin-bottom:12px;white-space:nowrap}
.contact-list svg{flex:none;margin-top:2px}
.footer .rule{position:absolute;left:100px;top:231px;width:1000px;height:1px;background:#444}
.footer .copy{position:absolute;left:100px;top:260px;font-size:12px}
.footer .social{position:absolute;left:948px;top:252px;gap:12px}
.footer .social i{width:32px;height:32px;border-color:#fff}
</style>
</head>
<body>
<div class="page">

<header class="header">
  <div class="brand">
    <div class="brand-mark"></div>
    <div>
      <div class="brand-name">Brisk Holloway</div>
      <div class="brand-tag">aviation security consulting</div>
    </div>
  </div>
  <div class="contact-strip">
    <span><svg width="16" height="16" viewBox="0 0 24 24"><path fill="#222" d="M6.6 10.8a15 15 0 0 0 6.6 6.6l2.2-2.2a1 1 0 0 1 1-.25 11 11 0 0 0 3.6.6 1 1 0 0 1 1 1V20a1 1 0 0 1-1 1A17 17 0 0 1 3 4a1 1 0 0 1 1-1h3.5a1 1 0 0 1 1 1c0 1.25.2 2.45.6 3.6a1 1 0 0 1-.25 1z"/></svg>1 800 555 0142</span>
    <span><svg width="16" height="14" viewBox="0 0 24 20"><rect x="1" y="1" width="22" height="18" fill="#222"/><path d="M2 3l10 8 10-8" stroke="#fff" stroke-width="2" fill="none"/></svg>info@briskholloway.example</span>
    <div class="social"><i></i><i></i><i></i><i></i></div>
  </div>
  <nav class="nav">
    <a class="active">Home</a><a>Who We Are</a><a>Our Services</a><a>Our Clients</a><a>Contact</a>
  </nav>
</header>

<section class="hero" role="img" aria-label="Photo of a passenger jet parked on the apron at dusk with ground crew">
  <h1>Brisk Holloway</h1>
  <p>Aviation Security Consulting Company</p>
  <a class="btn"><b>Read More</b><span class="arrow"><svg width="18" height="16" viewBox="0 0 18 16"><path d="M1 8h14M9 2l6 6-6 6" stroke="#fff" stroke-width="3" fill="none"/></svg></span></a>
  <div class="dots"><i class="on"></i><i></i><i></i><i></i></div>
</section>

<section class="welcome">
  <h2>Welcome to <em>Brisk Holloway</em></h2>
  <p class="lead">Brisk Holloway is a full service aviation security consulting company with experience in over 60 countries. We work with government and industry stakeholders to deliver outstanding security outcomes at both a regulatory and operational level.</p>

  <div class="feature" style="left:89px">
    <div class="diamond"><svg width="44" height="44" viewBox="0 0 44 44" fill="none" stroke="#fff" stroke-width="4"><path d="M6 6l32 32M38 6L6 38"/><path d="M6 16V6h10M28 6h10v10M38 28v10H28M16 38H6V28"/></svg></div>
    <h3>Flexibility</h3>
    <p>In depth knowledge built through years of experience brings the ability to deliver expertise to all areas of aviation</p>
    <a>READ MORE &gt;&gt;</a>
  </div>
  <div class="feature" style="left:347px">
    <div class="diamond"><svg width="40" height="44" viewBox="0 0 40 44"><path d="M10 20v-7a10 10 0 0 1 20 0v7" stroke="#fff" stroke-width="5" fill="none"/><rect x="5" y="20" width="30" height="22" rx="3" fill="#fff"/></svg></div>
    <h3>Safety</h3>
    <p>In depth knowledge built through years of experience brings the ability to deliver expertise to all areas of aviation</p>
    <a>READ MORE &gt;&gt;</a>
  </div>
  <div class="feature" style="left:606px">
    <div class="diamond"><svg width="44" height="44" viewBox="0 0 44 44" fill="#fff"><rect x="4" y="20" width="8" height="20"/><path d="M15 20l8-14c3 0 5 2 4 6l-2 6h11c3 0 4 3 3 5l-4 14c-1 2-2 3-4 3H15z"/></svg></div>
    <h3>Quality</h3>
    <p>In depth knowledge built through years of experience brings the ability to deliver expertise to all areas of aviation</p>
    <a>READ MORE &gt;&gt;</a>
  </div>
  <div class="feature" style="left:865px">
    <div class="diamond"><svg width="48" height="40" viewBox="0 0 48 40" fill="#fff"><circle cx="24" cy="10" r="8"/><circle cx="9" cy="14" r="6"/><circle cx="39" cy="14" r="6"/><path d="M12 38a12 12 0 0 1 24 0z"/><path d="M0 36a9 9 0 0 1 14-8l-2 8zM48 36a9 9 0 0 0-14-8l2 8z"/></svg></div>
    <h3>Qualified Team</h3>
    <p>In depth knowledge built through years of experience brings the ability to deliver expertise to all areas of aviation</p>
    <a>READ MORE &gt;&gt;</a>
  </div>
</section>

<section class="services">
  <h2 class="section-title">Our <em>Services</em></h2>
  <div class="pager" style="left:1019px"><svg width="10" height="14" viewBox="0 0 10 14"><path d="M8 1L2 7l6 6" stroke="#fff" stroke-width="2.5" fill="none"/></svg></div>
  <div class="pager" style="left:1065px"><svg width="10" height="14" viewBox="0 0 10 14"><path d="M2 1l6 6-6 6" stroke="#fff" stroke-width="2.5" fill="none"/></svg></div>

  <article class="card" style="left:100px">
    <div class="pic" role="img" aria-label="Illustration of compliance icons connected over a blue world map" style="background:linear-gradient(135deg,#0a2a6e,#1f7fd6)"></div>
    <h3>Regulation and Compilance</h3>
    <p>In addition, civil aviation authorities are required to ensure these regulations are appropriately implemented..</p>
    <a class="btn"><b>Read More</b><span class="arrow"><svg width="14" height="12" viewBox="0 0 18 16"><path d="M1 8h14M9 2l6 6-6 6" stroke="#fff" stroke-width="3" fill="none"/></svg></span></a>
  </article>
  <article class="card" style="left:353px">
    <div class="pic" role="img" aria-label="Photo of a tablet showing charts on a desk with printed reports" style="background:linear-gradient(135deg,#e9eaee,#b9bfcc)"></div>
    <h3>Risk Assessment</h3>
    <p>In addition, civil aviation authorities are required to ensure these regulations are appropriately implemented..</p>
    <a class="btn"><b>Read More</b><span class="arrow"><svg width="14" height="12" viewBox="0 0 18 16"><path d="M1 8h14M9 2l6 6-6 6" stroke="#fff" stroke-width="3" fill="none"/></svg></span></a>
  </article>
  <article class="card" style="left:607px">
    <div class="pic" role="img" aria-label="Photo of a businessman touching a glowing digital security interface" style="background:linear-gradient(135deg,#2b3f6a,#6f8fc4)"></div>
    <h3>Cyber Security</h3>
    <p>In addition, civil aviation authorities are required to ensure these regulations are appropriately implemented..</p>
    <a class="btn"><b>Read More</b><span class="arrow"><svg width="14" height="12" viewBox="0 0 18 16"><path d="M1 8h14M9 2l6 6-6 6" stroke="#fff" stroke-width="3" fill="none"/></svg></span></a>
  </article>
  <article class="card" style="left:862px">
    <div class="pic" role="img" aria-label="Abstract blue network of connected lines" style="background:linear-gradient(135deg,#0b4fa8,#3fb0ef)"></div>
    <h3>Technology Evaluation</h3>
    <p>In addition, civil aviation authorities are required to ensure these regulations are appropriately implemented..</p>
    <a class="btn"><b>Read More</b><span class="arrow"><svg width="14" height="12" viewBox="0 0 18 16"><path d="M1 8h14M9 2l6 6-6 6" stroke="#fff" stroke-width="3" fill="none"/></svg></span></a>
  </article>
</section>

<section class="quote">
  <svg class="chev" style="left:100px" width="14" height="24" viewBox="0 0 14 24"><path d="M12 2L3 12l9 10" stroke="#fff" stroke-width="3" fill="none"/></svg>
  <div class="qmark">&ldquo;</div>
  <div class="portrait" role="img" aria-label="Portrait photo of the quoted executive"></div>
  <blockquote>&ldquo; Sed ut perspiciatis unde omnis iste natus error sit voluptatem accusantium doloremque laudantium, totam rem aperiam, eaque ipsa quae ab illo inventore veritatis et quasi architecto beatae vitae dicta sunt explicabo. Nemo enim ipsam voluptatem quia uuseq &rdquo;</blockquote>
  <cite>- MARTIN HALE</cite>
  <svg class="chev" style="left:1087px" width="14" height="24" viewBox="0 0 14 24"><path d="M2 2l9 10-9 10" stroke="#fff" stroke-width="3" fill="none"/></svg>
</section>

<section class="industries">
  <h2 class="section-title">Industry &amp; Sector <em>we serve are</em></h2>
  <div class="tile" style="left:100px;top:1759px;background:linear-gradient(160deg,#8fb3d9,#9a8a6e)" role="img" aria-label="Photo of a city road with traffic barriers and taxis"><span>Government Capability</span></div>
  <div class="tile" style="left:437px;top:1759px;background:linear-gradient(180deg,#3a3f4a,#7a5a30)" role="img" aria-label="Night photo of a lit industrial waterfront"><span>High Threat Environment</span></div>
  <div class="tile" style="left:774px;top:1759px;background:linear-gradient(180deg,#d58a5a,#2b4a7a)" role="img" aria-label="Dusk photo of an oil and gas terminal with storage tanks"><span>Oil and Gas</span></div>
  <div class="tile" style="left:100px;top:1981px;background:linear-gradient(180deg,#b9d2e6,#6d7a6a)" role="img" aria-label="Aerial photo of a highway interchange and bridge"><span>Transport</span></div>
  <div class="tile" style="left:437px;top:1981px;background:linear-gradient(160deg,#eaf2fb,#7d94b3)" role="img" aria-label="Photo of a man looking up at glass skyscrapers"><span>Urban Planning</span></div>
  <div class="tile" style="left:774px;top:1981px;background:linear-gradient(160deg,#6f7c8d,#2b3340)" role="img" aria-label="Photo of architects reviewing a building model"><span>Critical Infrastructure</span></div>
  <div class="view-more">VIEW MORE &gt;&gt;</div>
</section>

<section class="clients">
  <h2 class="section-title">Our Clients</h2>
  <svg class="abs" style="left:100px;top:140px" width="12" height="22" viewBox="0 0 12 22"><path d="M10 2L2 11l8 9" stroke="#999" stroke-width="2" fill="none"/></svg>
  <div class="client" style="left:150px"><i></i>Crestline</div>
  <div class="client" style="left:332px"><i></i>Skyward Union</div>
  <div class="client" style="left:516px"><i></i>Aerovane</div>
  <div class="client" style="left:701px"><i></i>Redstone Assured</div>
  <div class="client" style="left:883px"><i></i>Civic Transit Office</div>
  <svg class="abs" style="left:1088px;top:140px" width="12" height="22" viewBox="0 0 12 22"><path d="M2 2l8 9-8 9" stroke="#999" stroke-width="2" fill="none"/></svg>
</section>

<footer class="footer">
  <div class="brand">
    <div class="brand-mark"></div>
    <div>
      <div class="brand-name">Brisk Holloway</div>
      <div class="brand-tag">aviation security consulting</div>
    </div>
  </div>
  <h4 style="left:434px">Information</h4>
  <ul class="links"><li>Home</li><li>Who we are</li><li>Our services</li><li>Our clients</li><li>Contact</li></ul>
  <div class="news">
    <h4 style="left:591px">Newsletter Subscription</h4>
    <p>Register your email address to get information about us</p>
    <div class="field">Email Address</div>
    <div class="subscribe">SUBSCRIBE</div>
  </div>
  <h4 style="left:916px">Contact Us</h4>
  <ul class="contact-list">
    <li><svg width="12" height="16" viewBox="0 0 12 16"><path d="M6 0a6 6 0 0 1 6 6c0 4-6 10-6 10S0 10 0 6a6 6 0 0 1 6-6z" fill="#fff"/><circle cx="6" cy="6" r="2.2" fill="#222"/></svg><span>410 Harbor Line Road<br>Chicago, IL 60601</span></li>
    <li><svg width="13" height="13" viewBox="0 0 24 24"><path fill="#fff" d="M6.6 10.8a15 15 0 0 0 6.6 6.6l2.2-2.2a1 1 0 0 1 1-.25 11 11 0 0 0 3.6.6 1 1 0 0 1 1 1V20a1 1 0 0 1-1 1A17 17 0 0 1 3 4a1 1 0 0 1 1-1h3.5a1 1 0 0 1 1 1c0 1.25.2 2.45.6 3.6a1 1 0 0 1-.25 1z"/></svg><span>1 800 555 0142</span></li>
    <li><svg width="13" height="13" viewBox="0 0 16 16"><rect x="1" y="5" width="14" height="9" fill="#fff"/><rect x="4" y="1" width="8" height="5" fill="#fff" stroke="#222"/></svg><span>1 800 555 0177</span></li>
    <li><svg width="13" height="11" viewBox="0 0 24 20"><rect x="1" y="1" width="22" height="18" fill="#fff"/><path d="M2 3l10 8 10-8" stroke="#222" stroke-width="2" fill="none"/></svg><span>info@briskholloway.example</span></li>
  </ul>
  <div class="rule"></div>
  <p class="copy">Copyrights © 2016, Brisk Holloway. All rights reserved.</p>
  <div class="social"><i></i><i></i><i></i><i></i></div>
</footer>

</div>
</body>
</html>
```